Personal Training, Nutrition and Habit Change

I am looking to create a memorable brand name and logo that describes what I offer..something like, "Bold Oak Daily" or "Kestrel Grove Fitness". I want people to know that they can come to me to elevate their lives through a balance of fitness, good nutrition and mental well-being through meditating, mindfulness and a program of stress relief.

Target Market(s)

Well established individuals who are interested in spending money for their health and well-being and making a long term commitment to themselves.

Industry/Entity Type

Fitness

Contact Information for Business Card

Would like a horizontal card, possibly in black with blue and white lettering with the logo that implies a figure running, moving fast or is agile. Would like a statement on the back about habit change and importance of fitness

Logo Text

Elevate Your Life and Well Being or Elevate Your Life and Well Being

Font styles to use
Sans Serif

Colors

Designer to choose colors to be used in the design.

Requirements
Must have
• A strong, powerful name (brand) for my company. Something short, powerful, memorable and relevant. A company motto that describes briefly what I'll help clients achieve, i.e. Elevate Your Life and Well Being, etc. A place for my name and multiple credentials with room for contact info of course. On the back, does it make practical sense to describe habit change, achieving balance making commitment to one's health and well being and finding great joy in one's daily life.
Nice to have
• Basically what I said above.
Should not have
• Just show me what you've got!

```html
<!DOCTYPE html>
<html lang="en">
<head>
<meta charset="UTF-8">
<title>Bold Oak Daily – Business Card</title>
<link href="https://fonts.googleapis.com/css2?family=Montserrat:wght@700;800&family=Roboto:wght@400;500&display=swap" rel="stylesheet">
<style>
  :root {
    --stage: #2b2b2d;
    --card-black: #0d0d0e;
    --card-white: #f7f7f7;
    --brand-blue: #1aa3e8;
    --ink: #141414;
    --ink-soft: #2a2a2a;
    --paper-text: #ffffff;
  }
  * { margin: 0; padding: 0; box-sizing: border-box; }
  html, body { width: 1200px; height: 902px; overflow: hidden; }
  body {
    background: var(--stage);
    font-family: "Roboto", Arial, sans-serif;
    position: relative;
  }
  .card {
    position: absolute;
    left: 300px;
    width: 600px;
    height: 343px;
    border-radius: 3px;
    box-shadow: 0 10px 28px rgba(0,0,0,0.45);
    overflow: hidden;
  }
  .card--back { top: 90px; background: var(--card-black); }
  .card--front { top: 469px; background: var(--card-white); }

  .brand { position: absolute; display: flex; align-items: center; gap: 14px; }
  .brand__dot {
    width: 40px; height: 40px; border-radius: 50%;
    background: var(--brand-blue); flex: none;
  }
  .brand__name {
    font-family: "Montserrat", Arial, sans-serif;
    font-weight: 700;
    font-size: 32px;
    color: var(--brand-blue);
    line-height: 1;
    white-space: nowrap;
  }
  .brand__motto {
    font-family: "Roboto", Arial, sans-serif;
    font-weight: 400;
    font-size: 18px;
    margin-top: 6px;
    line-height: 1.1;
    white-space: nowrap;
  }

  .card--back .brand { left: 120px; top: 96px; }
  .card--back .brand__motto { color: var(--paper-text); }
  .statement {
    position: absolute;
    left: 56px; right: 56px; bottom: 60px;
    color: var(--paper-text);
    font-size: 14px;
    line-height: 1.55;
  }

  .card--front .brand { left: 72px; top: 66px; }
  .card--front .brand__motto { color: var(--ink-soft); }
  .rule-top {
    position: absolute; left: 230px; right: 40px; top: 150px;
    height: 1.5px; background: var(--ink);
  }
  .person { position: absolute; left: 40px; bottom: 44px; }
  .person__rule { width: 250px; height: 1.5px; background: var(--ink); margin-bottom: 12px; }
  .person__name {
    font-family: "Montserrat", Arial, sans-serif;
    font-weight: 800; font-size: 30px; color: var(--ink); line-height: 1;
  }
  .person__role {
    font-family: "Montserrat", Arial, sans-serif;
    font-weight: 700; font-size: 15px; color: var(--brand-blue);
    letter-spacing: 0.5px; margin-top: 4px;
  }
  .contacts { position: absolute; left: 340px; top: 176px; list-style: none; }
  .contacts li {
    display: flex; align-items: center; gap: 10px;
    font-size: 17px; color: var(--ink); margin-bottom: 7px;
    white-space: nowrap;
  }
  .contacts svg { width: 22px; height: 22px; flex: none; }
</style>
</head>
<body>

<section class="card card--back" aria-label="Card back">
  <div class="brand">
    <span class="brand__dot"></span>
    <div>
      <div class="brand__name">Bold Oak Daily</div>
      <div class="brand__motto">Elevate Your Life and Well Being</div>
    </div>
  </div>
  <p class="statement">Does it make practical sense to describe habit change, achieving balance making commitment to one's health and well being and finding great joy in one's daily life</p>
</section>

<section class="card card--front" aria-label="Card front">
  <div class="brand">
    <span class="brand__dot"></span>
    <div>
      <div class="brand__name">Bold Oak Daily</div>
      <div class="brand__motto">Elevate Your Life and Well Being</div>
    </div>
  </div>
  <div class="rule-top"></div>

  <div class="person">
    <div class="person__rule"></div>
    <div class="person__name">MARCUS HALE</div>
    <div class="person__role">MANAGING DIRECTOR</div>
  </div>

  <ul class="contacts">
    <li>
      <svg viewBox="0 0 22 22" aria-hidden="true"><circle cx="11" cy="11" r="11" fill="#1aa3e8"/><path d="M7.5 6.5l2 0 1 2.6-1.3 1c.6 1.3 1.5 2.2 2.8 2.8l1-1.3 2.6 1v2c0 .6-.5 1-1 1C9.6 15.6 6.4 12.4 6.4 7.5c0-.6.5-1 1.1-1z" fill="#fff"/></svg>
      <span>555.214.7730</span>
    </li>
    <li>
      <svg viewBox="0 0 22 22" aria-hidden="true"><circle cx="11" cy="11" r="11" fill="#1aa3e8"/><rect x="5.5" y="7.5" width="11" height="7.5" rx="1" fill="#fff"/><path d="M5.8 8l5.2 4 5.2-4" fill="none" stroke="#1aa3e8" stroke-width="1.2"/></svg>
      <span>info@boldoakdaily.com</span>
    </li>
    <li>
      <svg viewBox="0 0 22 22" aria-hidden="true"><circle cx="11" cy="11" r="11" fill="#1aa3e8"/><g fill="none" stroke="#fff" stroke-width="1.2"><circle cx="11" cy="11" r="5.5"/><ellipse cx="11" cy="11" rx="2.4" ry="5.5"/><path d="M5.5 11h11M6.3 8.2h9.4M6.3 13.8h9.4"/></g></svg>
      <span>www.boldoakdaily.com</span>
    </li>
  </ul>
</section>

</body>
</html>
```